quillnest.com redesign with wireframes, white space and custom form are very important

Need a new two column design that will convert easily to mobile responsive. Lots of white space. Winning design will probably be based on header area and making the custom form stand out. I want the header to be very much like www.tamvorlo.com except the form not to go up into the header.
Here are some of the websites I really like:
www.brisketdoors.com
http://plinkaroofsdirect.com/
http://dorvikamplandings.com/

We buy homes for cash and close fast. Our target is a home seller who is desperate to sell quickly.
I have uploaded my really ugly wireframe and my logo. I also uploaded my photo for the about us box and a possible photo to use for the header.
The copy on the wireframe is what I will be using except for the about us box.

Here is the exact link for video to frame in the top left box.
https://vidnook.example/Qp39xatLbRr

Number of Pages Required

1 page

Font styles to use
Sans Serif

Colors
0592cd
85cae6
eaf1f7
fbee3d
ec1f27

Requirements
Must have
• Everything on wireframe.
• Must use Verdana font and nothing should be smaller than 12 point. Most should be in 14 point. (except maybe inside of form)

```html
<!DOCTYPE html>
<html lang="en">
<head>
<meta charset="utf-8">
<title>quillnest.com – Sell Your Home For Cash</title>
<link href="https://fonts.googleapis.com/css2?family=Open+Sans:ital,wght@0,400;0,600;0,700;0,800;1,600;1,700&display=swap" rel="stylesheet">
<style>
:root{
  --blue:#1a8ed6;
  --blue-dark:#0b74bf;
  --blue-light:#2aa6ea;
  --red:#e3262b;
  --ink:#333;
  --muted:#666;
  --line:#d9d9d9;
  --panel:#f3f3f3;
  --footer:#262626;
}
*{box-sizing:border-box;margin:0;padding:0}
html,body{width:1200px;height:2639px;overflow:hidden;background:#fff}
body{position:relative;font-family:"Open Sans",Verdana,sans-serif;color:var(--ink)}
.abs{position:absolute}
/* header */
.brand{left:100px;top:36px;font-size:34px;font-weight:800;color:var(--red);letter-spacing:-.5px}
.brand-mark{display:inline-block;width:14px;height:14px;background:var(--red);margin-right:8px;vertical-align:middle}
.main-nav{left:267px;top:88px;display:flex;gap:28px;font-size:15px;font-weight:700;color:#222}
.call{right:98px;top:36px;text-align:right}
.call-label{color:var(--red);font-weight:700;font-size:16px}
.call-hours{font-size:14px;color:#333;margin-top:6px}
.call-phone{color:var(--red);font-weight:700;font-size:16px;margin-top:8px}
/* hero */
.hero{left:100px;top:141px;width:1002px;height:440px;
  background:linear-gradient(180deg,#2c5fb6 0%,#4d86cf 30%,#c9ced4 45%,#e7e7e4 62%,#3e5a2c 78%,#2e4422 100%)}
.hero-title{left:100px;top:268px;width:1002px;text-align:center;color:#fff;font-size:40px;font-weight:800;text-shadow:0 2px 6px rgba(0,0,0,.55)}
.hero-sub{left:100px;top:332px;width:1002px;text-align:center;color:#fff;font-size:24px;font-weight:700;font-style:italic;text-shadow:0 2px 4px rgba(0,0,0,.5)}
.hero-arrow{top:306px;width:34px;height:44px;background:rgba(0,0,0,.35);display:flex;align-items:center;justify-content:center}
/* form */
.lead-form{left:635px;top:470px;width:423px;height:646px;background:linear-gradient(180deg,var(--blue-light),var(--blue-dark));padding:22px 24px;border-radius:3px;box-shadow:0 2px 8px rgba(0,0,0,.25)}
.form-title{color:#fff;text-align:center;font-size:21px;font-weight:700}
.form-sub{color:#dff1fc;text-align:center;font-size:15px;margin:4px 0 14px}
.field{display:block;width:100%;height:58px;border:0;background:#fff;margin-bottom:8px;padding:0 18px;font:13px "Open Sans",sans-serif;color:#444}
.field::placeholder{color:#444}
.submit{display:block;width:100%;height:52px;margin-top:14px;border:0;border-radius:3px;background:linear-gradient(180deg,#4a4a4a,#050505);color:#fff;font:700 20px "Open Sans",sans-serif;letter-spacing:.5px}
/* benefits */
.benefits-title{left:100px;top:616px;width:520px;font-size:30px;line-height:38px;font-weight:800;color:var(--blue)}
.benefit-list{left:100px;top:708px;list-style:none;font-size:16px;color:var(--red)}
.benefit-list li{display:flex;align-items:center;gap:12px;margin-bottom:9px}
.watch{left:100px;top:816px;font-size:16px;color:#333}
.video{left:100px;top:875px;width:500px;height:241px;background:linear-gradient(90deg,#8db5e0 0%,#6e8fb8 35%,#5a6e8a 55%,#bfe8f2 80%,#e9f8fb 100%)}
.play{left:300px;top:967px;width:100px;height:58px;background:rgba(20,20,20,.8);border-radius:8px;display:flex;align-items:center;justify-content:center}
/* panels */
.panel{background:linear-gradient(180deg,#fff,#f0f0f0);border:1px solid var(--line);border-radius:3px}
.intro{left:100px;top:1156px;width:500px;height:572px;padding:20px 22px}
.intro-lead{font-size:22px;line-height:31px;color:var(--blue)}
.intro-body{font-size:12px;line-height:21px;color:#555;margin-top:22px}
.intro-h{font-size:21px;font-weight:700;color:var(--blue);margin-top:22px}
.reasons{list-style:none;font-size:14px;margin-top:14px}
.reasons li{display:flex;align-items:center;gap:14px;margin-bottom:9px}
.help{font-size:41px;font-weight:700;color:var(--blue);margin-top:12px}
.fastest{font-size:21px;font-weight:700;color:#222;margin-top:2px;padding-left:4px}
.privacy{left:635px;top:1160px;width:229px;height:62px;background:var(--blue);color:#fff;font-size:15px;font-weight:700;display:flex;align-items:center;justify-content:center}
.social{top:1163px;width:56px;height:56px;border-radius:50%;border:3px solid #ddd}
.callbox{left:635px;top:1242px;width:467px;height:60px;font-size:17px;display:flex;align-items:center;padding-left:20px}
.card-head{height:48px;background:linear-gradient(180deg,var(--blue-light),var(--blue-dark));color:#fff;font-size:21px;font-weight:700;padding:8px 18px}
.testimonials{left:635px;top:1330px;width:467px;height:166px}
.quote{font-size:12px;line-height:20px;color:#888;padding:10px 18px 0}
.author{left:656px;top:1452px;font-size:14px;font-style:italic;color:#333}
.more{left:928px;top:1443px;width:156px;height:30px;border-radius:15px;background:var(--blue);color:#fff;font-size:12px;display:flex;align-items:center;justify-content:center}
.about{left:635px;top:1519px;width:467px;height:209px}
.about-text{font-size:12px;line-height:18px;color:#555;padding:8px 18px}
.about-photo{left:660px;top:1627px;width:90px;height:88px;background:linear-gradient(180deg,#6d8fb4,#c79a82 60%,#3d5a7a)}
/* posts */
.post{left:100px;width:500px;height:162px}
.post-img{position:absolute;left:16px;top:18px;width:130px;height:124px}
.post-title{position:absolute;left:162px;top:18px;font-size:17px;color:var(--blue)}
.post-date{position:absolute;left:162px;top:46px;font-size:12px;color:#555}
.post-text{position:absolute;left:162px;top:72px;width:310px;font-size:12px;line-height:19px;color:#333}
.cities{left:635px;top:1769px;width:467px;height:521px;padding:22px 26px}
.cities-h{font-size:21px;line-height:29px;color:var(--blue)}
.cities p{font-size:12px;line-height:20px;color:#555;margin-top:20px}
.cities p+p{margin-top:42px}
.links{left:100px;top:2320px;width:500px;height:183px;padding:14px 20px}
.links ul{list-style:none;font-size:12px;color:var(--blue)}
.links li{display:flex;align-items:center;gap:12px;height:26px}
.illus{left:308px;top:2328px;width:220px;height:172px;background:linear-gradient(180deg,#e6e6e6,#d94e2e 40%,#f2f2f2 60%,#bdbdbd)}
.photo-card{left:635px;top:2320px;width:467px;height:183px}
.photo{left:658px;top:2337px;width:294px;height:113px;background:linear-gradient(180deg,#b8d3ea,#5c7a47 45%,#8a8c86 75%,#5f7a3e)}
.photo-cap{left:660px;top:2464px;font-size:16px;color:var(--blue)}
.site-footer{left:0;top:2541px;width:1200px;height:98px;background:var(--footer)}
.foot-nav{left:0;top:2572px;width:1200px;display:flex;justify-content:center;gap:22px;font-size:12px;color:#aaa}
.copy{left:0;top:2598px;width:1200px;text-align:center;font-size:12px;color:#888}
</style>
</head>
<body>
<header>
  <div class="abs brand"><span class="brand-mark"></span>quillnest.com</div>
  <nav class="abs main-nav"><span>SELL YOUR HOME</span><span>HOW IT WORKS</span><span>STOP FORECLOSURE</span><span>PROBATE</span><span>CONTACT</span></nav>
  <div class="abs call"><div class="call-label">CALL US</div><div class="call-hours">Nights and weekends ok</div><div class="call-phone">555-014-2296</div></div>
</header>

<div class="abs hero" role="img" aria-label="Photo of a white single-storey house with shrubs under a blue sky"></div>
<div class="abs hero-title">SELL YOUR HOME FOR CASH IN 8 DAYS</div>
<div class="abs hero-sub">WE BUY HOUSES NATIONWIDE.</div>
<div class="abs hero-arrow" style="left:106px"><svg width="14" height="20" viewBox="0 0 14 20"><path d="M11 2 3 10l8 8" fill="none" stroke="#fff" stroke-width="2.5"/></svg></div>
<div class="abs hero-arrow" style="left:1052px"><svg width="14" height="20" viewBox="0 0 14 20"><path d="m3 2 8 8-8 8" fill="none" stroke="#fff" stroke-width="2.5"/></svg></div>

<form class="abs lead-form">
  <div class="form-title">YES, I WANT TO SELL MY HOME FAST!</div>
  <div class="form-sub">Get a no obligation written offer in 36 hours</div>
  <input class="field" placeholder="Your Name">
  <input class="field" placeholder="Your phone number">
  <input class="field" placeholder="Your Email Address">
  <input class="field" placeholder="Property Address including City, State and Zip Code">
  <input class="field" placeholder="Repairs needed if any">
  <input class="field" placeholder="Asking price">
  <input class="field" placeholder="Comments">
  <button class="submit" type="button">SUBMIT</button>
</form>

<h2 class="abs benefits-title">THESE ARE THE BENEFITS OF SELLING YOUR HOME TO US.</h2>
<ul class="abs benefit-list">
  <li><svg width="14" height="14"><circle cx="7" cy="7" r="7" fill="#222"/><path d="M4 7h6M7.5 4.5 10 7l-2.5 2.5" stroke="#fff" stroke-width="1.6" fill="none"/></svg>You pick the closing date</li>
  <li><svg width="14" height="14"><circle cx="7" cy="7" r="7" fill="#222"/><path d="M4 7h6M7.5 4.5 10 7l-2.5 2.5" stroke="#fff" stroke-width="1.6" fill="none"/></svg>You pay NO commissions or fees</li>
  <li><svg width="14" height="14"><circle cx="7" cy="7" r="7" fill="#222"/><path d="M4 7h6M7.5 4.5 10 7l-2.5 2.5" stroke="#fff" stroke-width="1.6" fill="none"/></svg>You don't have to paint, clean or make repairs</li>
</ul>
<p class="abs watch">Watch to see our president Marvin explain how easy it is to sell to us.</p>
<div class="abs video" role="img" aria-label="Video still of the company president in front of a house"></div>
<div class="abs play"><svg width="22" height="24"><path d="M2 2l18 10L2 22z" fill="#fff"/></svg></div>

<section class="abs panel intro">
  <p class="intro-lead">Sell your home or house fast for cash to a professional investor company. We buy Houses and close quickly.</p>
  <p class="intro-body">Selling a home on your own has never been easier. From Orlando to Greensboro - and all points in between- you can sell your home today without any hassles. Call 1-800-555-0147 or fill out the form below to get a written offer on your home in just 36 hours. Sell today online to people that care.</p>
  <h3 class="intro-h">If you need to sell a home fast because of:</h3>
  <ul class="reasons">
    <li><svg width="12" height="12"><circle cx="6" cy="6" r="6" fill="#222"/><path d="M3 6h5M6 3.8 8.2 6 6 8.2" stroke="#fff" stroke-width="1.4" fill="none"/></svg>Divorce or Bankruptcy</li>
    <li><svg width="12" height="12"><circle cx="6" cy="6" r="6" fill="#222"/><path d="M3 6h5M6 3.8 8.2 6 6 8.2" stroke="#fff" stroke-width="1.4" fill="none"/></svg>Foreclosure</li>
    <li><svg width="12" height="12"><circle cx="6" cy="6" r="6" fill="#222"/><path d="M3 6h5M6 3.8 8.2 6 6 8.2" stroke="#fff" stroke-width="1.4" fill="none"/></svg>Landlord problems - evictions with tenants okay</li>
    <li><svg width="12" height="12"><circle cx="6" cy="6" r="6" fill="#222"/><path d="M3 6h5M6 3.8 8.2 6 6 8.2" stroke="#fff" stroke-width="1.4" fill="none"/></svg>Inherited property in probate</li>
    <li><svg width="12" height="12"><circle cx="6" cy="6" r="6" fill="#222"/><path d="M3 6h5M6 3.8 8.2 6 6 8.2" stroke="#fff" stroke-width="1.4" fill="none"/></svg>Termites, mold, flood or fire damage, leaky roof</li>
    <li><svg width="12" height="12"><circle cx="6" cy="6" r="6" fill="#222"/><path d="M3 6h5M6 3.8 8.2 6 6 8.2" stroke="#fff" stroke-width="1.4" fill="none"/></svg>Moving or can't afford mortgage payments</li>
  </ul>
  <div class="help">We Can Help.</div>
  <div class="fastest">We are the fastest home buyers around.</div>
</section>

<div class="abs privacy">OUR PRIVACY POLICY</div>
<div class="abs social" style="left:915px;background:#2f5597"></div>
<div class="abs social" style="left:980px;background:#c9302c"></div>
<div class="abs social" style="left:1045px;background:#2aa3e0"></div>
<div class="abs panel callbox">Call us 8am to 10 pm Eastern time. We answer our phones.</div>

<section class="abs panel testimonials">
  <div class="card-head">Home Seller Testimonials</div>
  <p class="quote">I just wanted to thank you for buying my home in Winter Park. You made it fast and easy and kept me well informed the whole way.</p>
</section>
<div class="abs author">Dalby Fenwick – Winter Park</div>
<div class="abs more">More Testimonials</div>

<section class="abs panel about">
  <div class="card-head">About Us</div>
  <p class="about-text">Owned and operated in Orlando Florida since 2001. Oldest Continuous operated website in country.</p>
</section>
<div class="abs about-photo" role="img" aria-label="Portrait photo of the company owner"></div>

<article class="abs panel post" style="top:1769px">
  <div class="post-img" role="img" aria-label="Photo of a two-storey suburban house" style="background:linear-gradient(180deg,#3d6fc0,#d8c9a8 55%,#5f8a3c)"></div>
  <div class="post-title">Lorem ipsum dolor</div><div class="post-date">May 04,2015</div>
  <p class="post-text">Nemo enim ipsam voluptatem quia voluptas sit aspernatur aut odit aut fugit, sed quia consequuntur magni dolores enesciunt.</p>
</article>
<article class="abs panel post" style="top:1948px">
  <div class="post-img" role="img" aria-label="Photo of a brick house" style="background:linear-gradient(180deg,#9ec0de,#7a4a36 50%,#4f6e34)"></div>
  <div class="post-title">Lorem ipsum dolor</div><div class="post-date">May 04,2015</div>
  <p class="post-text">Nemo enim ipsam voluptatem quia voluptas sit aspernatur aut odit aut fugit, sed quia consequuntur magni dolores enesciunt.</p>
</article>
<article class="abs panel post" style="top:2131px">
  <div class="post-img" role="img" aria-label="Photo of a large family house" style="background:linear-gradient(180deg,#2f62b4,#cdbb96 55%,#446e2e)"></div>
  <div class="post-title">Lorem ipsum dolor</div><div class="post-date">May 04,2015</div>
  <p class="post-text">Nemo enim ipsam voluptatem quia voluptas sit aspernatur aut odit aut fugit, sed quia consequuntur magni dolores enesciunt.</p>
</article>

<section class="abs panel cities">
  <h3 class="cities-h">Some of the cities where we buy houses. Not all are listed.</h3>
  <p>These are the cities where we have an affiliate where you can sell a home fast or quickly and we buy homes: Orlando Jacksonville Ft Myers Tampa St Pete Gainesville Tallahassee Melbourne West Palm Beach Apopka Deland Kissimmee Lakeland Ocala Chicago Philadelphia Camden Atlanta Valdosta Houston Detroit Phoenix Seattle Tacoma Portland Charlotte Cincinnati San Antonio Harrisburg Virginia Beach Virginia Homes Greensboro Charleston SC Flint Rochester Lake Florida Wilmington Columbia Titusville If you don't see your city, we still probably buy homes there.</p>
  <p>These are the types of real estate that we buy: We buy nice houses and outdated problem homes. We buy in great neighborhoods and not so nice. We buy block homes and frame homes. We buy</p>
</section>

<section class="abs panel links">
  <ul>
    <li><svg width="14" height="12"><path d="M1 6l4 4 8-9" stroke="#3aa635" stroke-width="2.6" fill="none"/></svg>Archives</li>
    <li><svg width="14" height="12"><path d="M1 6l4 4 8-9" stroke="#3aa635" stroke-width="2.6" fill="none"/></svg>Sell my house</li>
    <li><svg width="14" height="12"><path d="M1 6l4 4 8-9" stroke="#3aa635" stroke-width="2.6" fill="none"/></svg>Fast cash for homes</li>
    <li><svg width="14" height="12"><path d="M1 6l4 4 8-9" stroke="#3aa635" stroke-width="2.6" fill="none"/></svg>We buy houses</li>
    <li><svg width="14" height="12"><path d="M1 6l4 4 8-9" stroke="#3aa635" stroke-width="2.6" fill="none"/></svg>Real Estate investor</li>
    <li><svg width="14" height="12"><path d="M1 6l4 4 8-9" stroke="#3aa635" stroke-width="2.6" fill="none"/></svg>Latest</li>
  </ul>
</section>
<div class="abs illus" role="img" aria-label="Illustration of a white house with a red roof"></div>

<section class="abs panel photo-card"></section>
<div class="abs photo" role="img" aria-label="Photo of a single-storey house with trees and a driveway"></div>
<p class="abs photo-cap">We buy nice pretty houses and some ugly ones as well.</p>

<footer class="abs site-footer"></footer>
<nav class="abs foot-nav"><span>SELL YOUR HOME</span><span>HOW IT WORKS</span><span>STOP FORECLOSURE</span><span>PROBATE</span><span>CONTACT</span></nav>
<div class="abs copy">© 2015 quillnest.com. All rights reserved.</div>
</body>
</html>
```